Flyer design for retail store owners

i would need to have a flyer design for my retail shop customers to show that I am a mailbox store that has all major shipping vendors to for their shipping needs. Ensuring that they can take advantage of opening a house account at the store and billed monthly, word document has all the details. Please use stock images for the notary public, passport photos, mailbox brass pictures of my actual mailboxes are listed in the pictures. I need to make it POP and WOW these retail store owners as I am using it to advertise the business

```html
<!DOCTYPE html>
<html lang="en">
<head>
<meta charset="utf-8">
<title>Private Mailbox Flyer</title>
<link href="https://fonts.googleapis.com/css2?family=Montserrat:ital,wght@0,400;0,500;0,600;0,700;0,800;1,700&display=swap" rel="stylesheet">
<style>
  :root{
    --navy:#0c2340;
    --orange:#f7891f;
    --orange-band:#ec7a22;
    --badge:#f0531f;
    --paper:#ffffff;
    --ink:#111111;
    --light-band:#ececec;
    --backdrop:#e4e5e7;
  }
  *{margin:0;padding:0;box-sizing:border-box}
  html,body{width:1200px;height:800px;overflow:hidden}
  body{background:var(--backdrop);font-family:'Montserrat',sans-serif;position:relative}
  .page{position:absolute;top:85px;width:450px;height:630px;background:var(--navy);overflow:hidden;color:var(--paper);box-shadow:0 6px 18px rgba(0,0,0,.25)}
  .page--front{left:122px}
  .page--back{left:626px}
  .page-art{position:absolute;inset:0}
  .abs{position:absolute}

  .headline{right:30px;top:200px;text-align:right;color:var(--ink);font-weight:700;font-size:30px;line-height:34px;letter-spacing:-.2px}
  .section-title{font-weight:700;font-size:14px;letter-spacing:.3px;display:inline-block;border-bottom:1.5px solid var(--paper);padding-bottom:1px}
  .offer{left:27px;top:270px;width:180px}
  .offer p{margin-top:8px;font-size:9px;line-height:11.4px}
  .about{right:30px;top:298px;width:190px;text-align:right}
  .about p{margin-top:8px;font-size:7.6px;line-height:10.2px}
  .deals-title{left:27px;top:440px;font-weight:700;font-size:9.4px;letter-spacing:.2px}

  .deals{left:27px;top:467px;width:320px;list-style:none}
  .deals li{position:relative;padding-left:16px;font-size:8.8px;line-height:11.4px;margin-bottom:6.5px}
  .deals li::before{content:"";position:absolute;left:0;top:2px;width:7px;height:7px;border-radius:50%;background:var(--paper);border:2px solid var(--navy)}
  .deals b{font-weight:700}
  .deals .wide{width:320px}

  .badge{left:318px;top:543px;width:110px;height:92px}
  .badge-text{left:322px;top:574px;width:100px;transform:rotate(-8deg);text-align:center;color:var(--paper);font-style:italic;font-weight:700;line-height:1.15}
  .badge-text .t1{font-size:6.6px;font-weight:500;letter-spacing:.3px}
  .badge-text .t2{font-size:6.4px}
  .badge-text .t3{font-size:9.6px;font-weight:800}

  .intro{left:29px;top:266px;width:395px;font-size:12.6px;line-height:15.8px;font-weight:400}
  .partners-band{left:0;top:427px;width:450px;height:104px;background:var(--light-band);color:var(--navy)}
  .partners-title{position:absolute;left:0;right:0;top:12px;text-align:center;font-weight:700;font-size:13px;letter-spacing:.3px}
  .partners-rule{position:absolute;left:125px;width:200px;top:33px;height:1.5px;background:var(--navy)}
  .partners-rule::after{content:"";position:absolute;left:73px;top:-1px;width:56px;height:3px;background:var(--orange)}
  .partner-list{position:absolute;left:0;right:0;top:58px;display:flex;justify-content:center;gap:18px;list-style:none}
  .partner-list li{font-weight:700;font-size:13px;color:var(--navy)}

  .contact-label{font-weight:700;font-size:13.5px;display:inline-block;border-bottom:1.5px solid var(--paper);padding-bottom:1px}
  .contact-value{margin-top:6px;font-size:13.5px;font-weight:500}
  .contact--address{left:27px;top:550px}
  .contact--phone{left:264px;top:550px}
  .contact-divider{left:224px;top:548px;width:1.5px;height:49px;background:var(--orange)}
</style>
</head>
<body>

<section class="page page--front">
  <svg class="page-art" width="450" height="630" viewBox="0 0 450 630">
    <defs>
      <linearGradient id="mailboxTone" x1="0" y1="0" x2="1" y2="1">
        <stop offset="0" stop-color="#9aa9b2"/>
        <stop offset="1" stop-color="#6f7f89"/>
      </linearGradient>
    </defs>
    <path d="M397,0 L450,0 L450,285 L270,285 C222,281 186,240 168,193 C262,186 372,118 397,0 Z" fill="var(--orange)"/>
    <path role="img" aria-label="Photo of a wall of private post office mailboxes with a letter in one slot" d="M0,0 L397,0 C372,118 262,186 168,193 L0,193 Z" fill="url(#mailboxTone)"/>
    <path d="M397,0 C372,118 262,186 168,193 L0,193" fill="none" stroke="#ffffff" stroke-width="1.2"/>
    <rect x="0" y="460" width="450" height="170" fill="var(--orange-band)"/>
  </svg>

  <h1 class="abs headline">Need a Private<br>Mailbox?</h1>

  <div class="abs offer">
    <h2 class="section-title">WE OFFER:</h2>
    <p>Now renting mailboxes on Maple Ridge Commons Shopping Center. We are offering all Maple Ridge Commons shopping center owners/employees an exclusive promo deal! $12 a month for 6-12 months leases! You get a mailbox in the shop, a book of stamps(20 count), 3 notarizations by appointment, 100 copies of black and white, and 100 copies of color. Please see associate for sign up!</p>
  </div>

  <div class="abs about">
    <h2 class="section-title">ABOUT US:</h2>
    <p>Renting a mail box is one of the most efficient and cost saving methods for receiving your mail and packages. Instead of having to worry about private security, weather conditions, sorting, and deliveries; all you have to do is pick-up your mail from our secured facility each day except Sundays. You will get a notification when mail arrives whether envelope or package, it will be scanned in daily which other mailbox stores do not offer! We offer onsite Notary Public with no appointments and onsite Passport Photos and can ship out same day.</p>
  </div>

  <h3 class="abs deals-title">CHECK OUT THESE OTHER DEALS!</h3>

  <ul class="abs deals">
    <li style="width:260px">As a retail owner, you know how important it is to keep your customers coming back - you will get <b>20%</b> discount for printing services.</li>
    <li style="width:240px">We duplicate keys for $2/each, our regular price charge is $4/each. Save up to <b>50%</b>!</li>
    <li>Lamination is also discounted at <b>10%</b> off.</li>
    <li><b>10%</b> off retail supplies ... must be minimum of 10$</li>
    <li class="wide">For house accounts -a 5% discount will be deducted monthly of billing change to invoicing PLUS we're giving another 5% of the discount if you upgrade and sign up for mailbox. <b>Great right?</b></li>
  </ul>

  <svg class="abs badge" viewBox="0 0 110 92">
    <polygon points="30,4 82,0 106,38 92,78 46,92 8,70 4,30" fill="var(--navy)" opacity=".85"/>
    <polygon points="32,8 80,4 102,40 88,74 46,86 12,66 8,32" fill="var(--badge)"/>
    <path d="M20,20 L96,14 M14,80 L90,74" stroke="#ffffff" stroke-width=".8" stroke-dasharray="5 3" opacity=".8"/>
  </svg>
  <div class="abs badge-text">
    <div class="t1">TAKE ADVANTAGE</div>
    <div class="t2">Of This Limited Time</div>
    <div class="t3">OFFER NOW!</div>
  </div>
</section>

<section class="page page--back">
  <svg class="page-art" width="450" height="630" viewBox="0 0 450 630">
    <defs>
      <linearGradient id="notaryTone" x1="0" y1="0" x2="1" y2="1">
        <stop offset="0" stop-color="#e9e4e6"/>
        <stop offset=".55" stop-color="#d9cfd2"/>
        <stop offset="1" stop-color="#3b4a7a"/>
      </linearGradient>
    </defs>
    <path role="img" aria-label="Photo of a notary public stamp, wax seal on a certificate, and a passport with boarding passes" d="M0,0 H450 V239 H232 C140,239 50,212 0,152 Z" fill="url(#notaryTone)"/>
    <path d="M0,152 C50,212 140,239 232,239 H450" fill="none" stroke="var(--orange)" stroke-width="1.5"/>
  </svg>

  <p class="abs intro">At Brisk Parcel Post, our goal is to make your shipping experience as convenient as possible. Whether you are shipping packages, documents, or packages, we are here to help. Whether you want to track your package or estimate the price of your package, it is easy for you. We are ready to handle all of your postal services! Get also the services you need; printing, copying, and stop in to purchase postage or shipping materials</p>

  <div class="abs partners-band">
    <h2 class="partners-title">SERVICE POINT PARTNERS</h2>
    <div class="partners-rule"></div>
    <ul class="partner-list">
      <li>Jetline</li>
      <li>Routewise</li>
      <li>Civic Mail</li>
      <li>Cargo Arrow</li>
    </ul>
  </div>

  <div class="abs contact--address">
    <h3 class="contact-label">Our address:</h3>
    <p class="contact-value">Lorem Ipsum is simpl</p>
  </div>
  <div class="abs contact-divider"></div>
  <div class="abs contact--phone">
    <h3 class="contact-label">Phone:</h3>
    <p class="contact-value">00 123 45689</p>
  </div>
</section>

</body>
</html>
```